International Fleet Management Firm Website

HaulwaveKenro is a Fleet Management Company that provides insight into customers fleets. We do this through web tools which we have developed which function through a client login screen to help ensure that corporates are able to stay on top of their fleets 24/7.
We are about to launch and are looking for a great new website to help us come out with bang! We would like a site that matches our values of ; Courage, integrity and leadership.
Although we have developed the app. We would also like to redesign the look of the site on the back end.
(1) We need to incorporate the new corporate colours
(2) Would like to create a better user experience.
The site that I would like to model ours after is;
www.belvanmotors.com (usa version)
Good Luck!!
Updates
Jusst added the .png version of the logo. Hopes this helps!
Industry/Entity Type
It Company
Look and feel

```html
<!DOCTYPE html>
<html lang="en">
<head>
<meta charset="utf-8">
<title>HaulwaveKenro – Fleet Management</title>
<link rel="stylesheet" href="https://fonts.googleapis.com/css2?family=Open+Sans:wght@400;600;700&family=Roboto+Condensed:wght@700&family=Questrial&display=swap">
<style>
  :root {
    --brand-red: #8e2626;
    --brand-blue: #2a8bc0;
    --nav-blue: #2f8fc4;
    --btn-blue: #3593c6;
    --ink: #2b2b2b;
    --paper: #f6f7f8;
    --section-bg: #e6e6e6;
    --footer-bg: #3d3d3d;
    --footer-bar: #555555;
    --white: #ffffff;
    --link-red: #c0281e;
  }
  * { margin: 0; padding: 0; box-sizing: border-box; }
  html, body { width: 1080px; height: 1200px; overflow: hidden; }
  body { position: relative; font-family: "Questrial", sans-serif; color: var(--ink); background: var(--section-bg); }
  .abs { position: absolute; }

  .header { left: 0; top: 0; width: 1080px; height: 106px; background: var(--brand-red); }
  .nav { left: 0; top: 106px; width: 1080px; height: 34px; background: var(--nav-blue); }
  .nav a { position: absolute; top: 10px; font: 12px Arial, sans-serif; color: var(--white); text-decoration: none; }

  .logo-card { left: 104px; top: 0; width: 222px; height: 152px; z-index: 3; }
  .logo-name { position: absolute; left: 0; width: 222px; top: 74px; text-align: center; font: 700 25px/32px "Open Sans", sans-serif; color: var(--brand-blue); letter-spacing: -0.5px; }
  .logo-mark { position: absolute; left: 97px; top: 28px; width: 28px; height: 28px; border-radius: 50%; background: var(--brand-blue); }
  .logo-tag { position: absolute; left: 0; width: 222px; top: 117px; text-align: center; font: 8.5px "Questrial", sans-serif; letter-spacing: 1.5px; color: #666; }

  .login-btn { top: 10px; height: 32px; border-radius: 3px; background: var(--btn-blue); border: 1px solid #1c6f9c; color: #0f4c70; font: 700 11.5px Arial, sans-serif; display: flex; align-items: center; padding-left: 10px; }
  .login-btn .go { position: absolute; right: 0; top: 0; width: 32px; height: 30px; border-left: 1px solid #1c6f9c; display: flex; align-items: center; justify-content: center; }
  .phone { right: 112px; top: 60px; font: 700 27px "Roboto Condensed", sans-serif; color: var(--white); }

  .hero { left: 0; top: 140px; width: 1080px; height: 502px;
    background: linear-gradient(180deg, #c9a487 0%, #d8b08c 25%, #c99a70 45%, #8a7462 62%, #5c5650 80%, #6b5f56 100%); }
  .hero-title { color: var(--white); font: 700 27px "Open Sans", sans-serif; text-shadow: 0 2px 3px rgba(0,0,0,.55); letter-spacing: -0.3px; }

  .card { top: 470px; width: 288px; height: 141px; background: var(--paper); padding: 7px 14px 8px 11px; }
  .card h3 { font: 600 19.5px/26px "Open Sans", sans-serif; color: var(--brand-blue); margin-bottom: 6px; white-space: nowrap; letter-spacing: -0.2px; }
  .card p { font-size: 9.6px; line-height: 13.6px; color: #333; letter-spacing: .35px; padding-left: 2px; }
  .card .more { position: absolute; right: 22px; bottom: 17px; font-size: 8.5px; color: var(--link-red); }

  .about { left: 0; top: 642px; width: 1080px; height: 309px;
    background: linear-gradient(180deg, #8fbdd6 0%, #e3e6e8 22%, #e6e6e6 100%); }
  .about h2 { position: absolute; top: 50px; font: 700 29px/38px "Open Sans", sans-serif; color: var(--brand-blue); }
  .about p { position: absolute; font-size: 11.6px; line-height: 14.4px; color: #222; width: 410px; letter-spacing: .2px; }
  .about .btn { position: absolute; top: 264px; width: 78px; height: 28px; background: var(--brand-red); color: var(--white); font: 9px Arial, sans-serif; display: flex; align-items: center; justify-content: center; gap: 4px; }

  .footer { left: 0; top: 951px; width: 1080px; height: 219px; background: var(--footer-bg); }
  .footer h4 { position: absolute; top: 12px; font: 700 21px/26px "Open Sans", sans-serif; color: var(--brand-blue); }
  .footer .links a { position: absolute; left: 119px; font: 11.2px/14px Arial, sans-serif; color: var(--white); text-decoration: none; }
  .divider { position: absolute; top: 45px; width: 1px; height: 144px; background: #2a2a2a; border-right: 1px solid #4a4a4a; }
  .field { position: absolute; left: 381px; width: 199px; height: 27px; background: #555; border: 1px solid #6a6a6a; color: #ddd; font: 9.5px "Questrial", sans-serif; padding-left: 12px; display: flex; align-items: center; letter-spacing: .3px; }
  .submit { position: absolute; left: 381px; top: 127px; width: 199px; height: 28px; background: var(--brand-red); border: 1px solid #b04040; color: var(--white); font: 600 13px "Open Sans", sans-serif; display: flex; align-items: center; justify-content: center; }
  .contact-logo { position: absolute; left: 745px; top: 47px; width: 223px; height: 32px; background: #d9d9d9; display: flex; align-items: center; padding-left: 10px; gap: 10px; font: 700 19px "Open Sans", sans-serif; color: var(--brand-blue); }
  .contact-logo .dot { width: 16px; height: 16px; background: var(--brand-blue); border-radius: 50%; }
  .contact-item { position: absolute; left: 745px; display: flex; gap: 8px; font: 10px Arial, sans-serif; color: var(--white); line-height: 13.6px; }
  .contact-item svg { flex: none; }

  .copyright { left: 0; top: 1170px; width: 1080px; height: 30px; background: var(--footer-bar); color: #e8e8e8; font: 8.5px Arial, sans-serif; text-align: center; line-height: 30px; letter-spacing: .3px; }
</style>
</head>
<body>

<header class="abs header"></header>
<nav class="abs nav">
  <a style="left:358px">HOME</a>
  <a style="left:422px">ABOUT US</a>
  <a style="left:510px">OUR SERVICES</a>
  <a style="left:625px">FLEET SOLUTION</a>
  <a style="left:751px">RESOURCE CENTER</a>
  <a style="left:895px">CONTACT US</a>
</nav>

<div class="abs logo-card">
  <svg width="222" height="152" viewBox="0 0 222 152" style="position:absolute;left:0;top:0">
    <path d="M1 0 H221 V136 L111 151 L1 136 Z" fill="#ffffff" stroke="#c9c9c9" stroke-width="1"/>
    <line x1="4" y1="108" x2="218" y2="108" stroke="#d0d0d0"/>
  </svg>
  <div class="logo-mark"></div>
  <div class="logo-name">HaulwaveKenro</div>
  <div class="logo-tag">We Make Sense of Your Fleet</div>
</div>

<div class="abs login-btn" style="left:702px;width:134px">FleetWeb Login
  <span class="go"><svg width="18" height="18" viewBox="0 0 18 18"><circle cx="9" cy="9" r="8" fill="#0f3f5c"/><path d="M5 9h7M9 5.5l3.5 3.5L9 12.5" stroke="#fff" stroke-width="2" fill="none"/></svg></span>
</div>
<div class="abs login-btn" style="left:848px;width:119px">Driver Login
  <span class="go"><svg width="18" height="18" viewBox="0 0 18 18"><circle cx="9" cy="9" r="8" fill="#0f3f5c"/><path d="M5 9h7M9 5.5l3.5 3.5L9 12.5" stroke="#fff" stroke-width="2" fill="none"/></svg></span>
</div>
<div class="abs phone">Call 24/7 (740) 555 XXXX</div>

<div class="abs hero" role="img" aria-label="Desert highway with a red box truck, red sedan, white semi truck, silver pickup and white delivery van lined up across the road"></div>
<div class="abs hero-title" style="left:266px;top:158px">Running an efficient fleet positively affects</div>
<div class="abs hero-title" style="right:112px;top:190px">the profitability of your organization</div>

<section class="abs card" style="left:104px">
  <h3>Strategic Fleet Management</h3>
  <p>Regardless of you industry, company or individual circumstance, HWK can help you achieve your Fleet Targets. Our team of professionals can help you run an optimal fleet using HWK 2.0 our in house Fleet Management Software.</p>
  <span class="more">Learn more ⁜</span>
</section>
<section class="abs card" style="left:400px">
  <h3>Total Cost Management</h3>
  <p>Costs are an ongoing challenge which needs to be constantly managed. Every decision taken has long term effects on your success. As your partner, HWK works with you to ensure that these costs stay under control all the time.</p>
  <span class="more">Learn more ⁜</span>
</section>
<section class="abs card" style="left:695px">
  <h3>Fuel Management</h3>
  <p>Regardless of you industry, company or individual circumstance, HWK can help you achieve your Fleet Targets. Our team of professionals can help you run an optimal fleet using HWK 2.0 our in house Fleet Management Software.</p>
  <span class="more">Learn more ⁜</span>
</section>

<section class="abs about">
  <h2 style="left:121px">WHO WE ARE</h2>
  <p style="left:120px;top:106px">HWK was formed to fill a need in the Fleet Management Industry. We aim to provide first class Fleet Management Services to organizations. Whether your fleet is owned, outsourced or a mixture – we aim to help you ensure that your costs stay controlled.<br><br>We also advise clients on vehicles and processes that will help improve your bottom line.<br><br>We provide organizations with company cars and trucks along with unmatched service and support.</p>
  <a class="btn" style="left:450px">Learn more <span style="color:#f2c230">➔</span></a>

  <h2 style="left:561px">FLEET ADMINISTRATION</h2>
  <p style="left:559px;top:106px">When it comes to choosing your fleet management partner, you want a leader with the experience and expertise to handle the many complexities. You want easy to use tools that provide rich data and insights. Mostly, you want reassurance that your fleet will run well on a day-to-day basis without you getting bogged down with the details. With HWK, you get exactly all this...and so much more.<br><br>We provide organizations with company cars and trucks along with unmatched service and support.</p>
  <a class="btn" style="left:890px">Learn more <span style="color:#f2c230">➔</span></a>
</section>

<footer class="abs footer">
  <h4 style="left:118px">Brows site</h4>
  <div class="links">
    <a style="top:44px">Home</a>
    <a style="top:65px">About Us</a>
    <a style="top:86px">Our services</a>
    <a style="top:107px">Fleet Solution</a>
    <a style="top:127px">Resource Center</a>
    <a style="top:148px">Contact us</a>
  </div>
  <div class="divider" style="left:296px"></div>

  <h4 style="left:410px">Let us call you</h4>
  <div class="field" style="top:46px">Enter your name</div>
  <div class="field" style="top:87px">Enter your email address</div>
  <div class="submit">Submit</div>
  <div class="divider" style="left:662px"></div>

  <h4 style="left:745px">Contact info</h4>
  <div class="contact-logo"><span class="dot"></span>HaulwaveKenro</div>
  <div class="contact-item" style="top:95px">
    <svg width="14" height="18" viewBox="0 0 14 18"><path d="M7 1a6 6 0 0 0-6 6c0 4.5 6 10 6 10s6-5.5 6-10a6 6 0 0 0-6-6z" fill="#bbb"/><circle cx="7" cy="7" r="2.3" fill="#3d3d3d"/></svg>
    <span>Lorem Ipsum. Proin gravida nibh vel<br>velit auctor aliquet. Aenean</span>
  </div>
  <div class="contact-item" style="top:139px">
    <svg width="14" height="16" viewBox="0 0 14 16"><rect x="2" y="0.5" width="10" height="15" rx="1.5" fill="#bbb"/><rect x="4" y="2.5" width="6" height="9" fill="#3d3d3d"/></svg>
    <span style="line-height:16px">(740) 555 XXXX</span>
  </div>
  <div class="contact-item" style="top:168px">
    <svg width="16" height="16" viewBox="0 0 16 16"><rect x="4" y="1" width="8" height="4" fill="#bbb"/><rect x="1" y="5" width="14" height="7" rx="1" fill="#bbb"/><rect x="4" y="10" width="8" height="5" fill="#ddd"/></svg>
    <span style="line-height:16px">(740) 555 XXXX</span>
  </div>
  <div class="contact-item" style="top:196px">
    <svg width="16" height="14" viewBox="0 0 16 14"><path d="M1 6l7-5 7 5v7H1z" fill="#bbb"/><path d="M1 6l7 4 7-4" stroke="#3d3d3d" fill="none"/></svg>
    <span style="line-height:14px">info@haulwavekenro.com</span>
  </div>
</footer>

<div class="abs copyright">(c) 2013. HaulwaveKenro, All Rights Reserved.</div>

</body>
</html>
```